Harbourgate Earthmoving – Website Design Brief

Web Design Brief

We are seeking a web designer to build a modern, responsive website for Harbourgate Earthmoving, a Sydney-based earthworks and excavation company.

2. Project Goal
- Build a professional, easy-to-navigate website that:
- Showcases HGE’s capabilities and past projects
- Attracts residential and commercial developers
- Builds credibility and encourages enquiries

3. Target Audience
- Residential developers and home builders
- Commercial construction firms
- Project managers seeking reliable excavation & plant hire services

4. Services to Highlight
- Bulk Excavation
- Detailed Excavation
- Demolition
- Shoring
- Plant Hire

5. Brand Style & Tone
- Clean, bold, and modern
- Professional with a “we get the job done” attitude
- Colors: Lime Green + Concrete Grey (from logo)
- Fonts: Match the modern, rounded, bold typeface in the logo
- Imagery: Showcase big machines, on-site work, before & after shots

6. Website Pages
Recommended structure:
- Home – Quick intro, project highlights, CTA
- About Us – Team story, mission, safety focus
- Services – Separate sections for each core service
- Projects – Case studies or photo gallery
- Plant Hire – Machines available, specs/photos
- Contact – Form + map + details

7. Assets Provided
- Logo (both long + stacked formats)
- Project photos. More can be provided if required.
- Copy: To be drafted

8. Deliverables
Responsive website (desktop/mobile/tablet)
- SEO-ready structure
- CMS (WordPress) for future edits
- Google Maps integration, job enquiry form

Target Market(s)

Target Audience Residential developers and home builders Commercial construction firms Project managers seeking reliable excavation & plant hire services

Industry/Entity Type

Construction

Number of Pages Required

1 page

Requirements
Must have
• Build a professional, easy-to-navigate website that: Showcases HGE’s capabilities and past projects Attracts residential and commercial developers Builds credibility and encourages enquiries
Nice to have
• All provided in the Description
Should not have

```html
<!DOCTYPE html>
<html lang="en">
<head>
<meta charset="utf-8">
<title>Harbourgate Earthmoving</title>
<link href="https://fonts.googleapis.com/css2?family=Syncopate:wght@400;700&family=Michroma&family=Montserrat:ital,wght@0,400;0,500;0,600;0,700;1,400&display=swap" rel="stylesheet">
<style>
:root{
  --lime:#7dc242;
  --lime-dark:#67a633;
  --concrete:#8f9091;
  --concrete-light:#b9b9b9;
  --paper:#ececec;
  --ink:#141414;
  --charcoal:#333435;
  --footer:#1c1c1c;
  --white:#ffffff;
  --muted:#9c9c9c;
}
*{box-sizing:border-box;margin:0;padding:0}
html,body{width:1200px;height:4484px;overflow:hidden}
body{font-family:"Montserrat",sans-serif;color:var(--ink);background:var(--paper);position:relative}
section,header,footer{position:absolute;left:0;width:1200px;overflow:hidden}
.abs{position:absolute}
.heading{position:absolute;font-family:"Syncopate",sans-serif;font-weight:700;font-size:33px;letter-spacing:1px;text-transform:uppercase;line-height:1;white-space:nowrap}
.heading .soft{color:var(--concrete)}
.centered{left:0;width:1200px;text-align:center}
.btn{position:absolute;background:var(--lime);color:var(--white);font-size:10.5px;font-weight:700;letter-spacing:1px;text-transform:uppercase;display:flex;align-items:center;justify-content:center;border-radius:2px;white-space:nowrap}
.wordmark{position:absolute;font-family:"Syncopate",sans-serif;font-weight:700;color:var(--lime);white-space:nowrap;line-height:1;letter-spacing:2px;font-size:40px}
.photo{position:absolute}

/* hero */
.hero{top:0;height:561px}
.hero-bg{inset:0;background:linear-gradient(100deg,#1d2a36 0%,#3a3b37 40%,#6b5843 75%,#4f4a40 100%)}
.hero-shade{inset:0;background:linear-gradient(90deg,rgba(10,14,20,.65) 0%,rgba(10,14,20,.15) 60%,rgba(0,0,0,0) 100%)}
.brand{position:absolute;font-family:"Syncopate",sans-serif;font-weight:700;color:var(--lime);letter-spacing:1px;white-space:nowrap}
.hero .brand{left:122px;top:33px;font-size:17px}
.nav{position:absolute;top:37px;left:0;width:1200px;height:20px}
.nav a{position:absolute;color:var(--white);font-size:10.5px;text-decoration:none;letter-spacing:.5px;text-transform:uppercase;white-space:nowrap}
.nav a.active{color:var(--lime);border-bottom:2px solid var(--lime);padding-bottom:6px}
.hero .welcome{left:122px;top:138px;font-family:"Michroma",sans-serif;color:var(--white);font-size:23px}
.hero .title{left:122px;top:186px;font-family:"Syncopate",sans-serif;font-weight:700;font-size:42px;line-height:1.2;color:var(--lime);white-space:nowrap}
.hero .tag{left:122px;top:366px;color:var(--white);font-size:12.5px;line-height:1.5;width:230px}
.hero .btn{left:122px;top:428px;width:198px;height:39px}

/* about */
.about{top:561px;height:522px;background:var(--paper)}
.about-ring{left:124px;top:68px;width:380px;height:380px;border-radius:50%;border:8px solid var(--lime)}
.about-photo{left:138px;top:82px;width:352px;height:352px;border-radius:50%;background:radial-gradient(circle at 40% 40%,#d8b84a 0%,#8b6d3e 45%,#5a4a38 100%)}
.badge{left:422px;top:303px;width:128px;height:128px;border-radius:50%;background:var(--lime);border:5px solid var(--paper);color:var(--white);text-align:center;display:flex;flex-direction:column;align-items:center;justify-content:center;font-weight:600;font-size:14px;line-height:1.2}
.badge svg{margin-bottom:6px}
.about .heading{left:672px;top:135px}
.about .copy{left:672px;top:180px;width:400px;font-size:11px;line-height:1.75;color:#333}
.about .copy p+p{margin-top:12px}
.about .btn{left:672px;top:346px;width:97px;height:32px}
.about .wordmark{left:432px;top:478px}

/* services */
.services{top:1083px;height:460px;background:linear-gradient(180deg,#8c8d8e,#9a9b9c)}
.services .heading{top:58px;color:var(--ink)}
.services .heading .soft{color:var(--white)}
.service-card{position:absolute;top:124px;width:230px;height:260px;overflow:visible}
.service-card .photo{inset:0}
.service-card .fade{position:absolute;inset:0;background:linear-gradient(180deg,rgba(0,0,0,0) 35%,rgba(0,0,0,.7) 100%)}
.service-card.active{outline:3px solid var(--lime)}
.service-icon{position:absolute;left:88px;top:140px;width:54px;height:54px;border-radius:50%;background:var(--white);display:flex;align-items:center;justify-content:center}
.service-name{position:absolute;left:0;width:100%;top:207px;text-align:center;color:var(--white);font-weight:700;font-size:13.5px;text-transform:uppercase}
.service-card.active .service-name{top:142px}
.service-desc{position:absolute;left:14px;right:14px;top:164px;text-align:center;color:var(--white);font-size:9.5px;line-height:1.5}
.service-card .btn{left:65px;top:248px;width:100px;height:24px;font-size:9.5px}
.arrow{position:absolute;width:26px;height:26px;border-radius:50%;background:rgba(255,255,255,.55);display:flex;align-items:center;justify-content:center}

/* team */
.team{top:1543px;height:544px;background:var(--paper)}
.team .heading{top:60px}
.team .intro{top:108px;left:300px;width:600px;text-align:center;font-size:11px;line-height:1.7;color:#333}
.team-photo-band{left:0;top:380px;width:1200px;height:164px;background:linear-gradient(180deg,rgba(236,236,236,1) 0%,#d6d7d8 45%,#b8bbbd 100%)}
.member{position:absolute;top:190px;width:174px;text-align:center}
.member .ring{margin:0 auto;width:174px;height:174px;border-radius:50%;border:2px solid var(--lime);padding:5px}
.member .face{width:100%;height:100%;border-radius:50%}
.member .name{margin-top:18px;font-size:13.5px;font-weight:600;text-transform:uppercase}
.member .bio{font-size:9px;color:var(--lime);letter-spacing:1px;text-transform:uppercase;margin-top:2px}

/* projects */
.projects{top:2087px;height:843px;background:var(--paper)}
.projects .heading{top:60px}
.projects .intro{top:105px;left:220px;width:760px;text-align:center;font-size:11px;line-height:1.7;color:#333}
.project{position:absolute;width:467px;height:257px}
.project .label{position:absolute;left:0;right:0;bottom:0;height:35px;background:rgba(30,30,30,.6);color:var(--white);font-weight:700;font-size:13.5px;text-transform:uppercase;display:flex;align-items:center;justify-content:center}
.projects .btn{left:519px;top:747px;width:161px;height:32px}
.projects .wordmark{left:0;width:1200px;text-align:center;top:797px}

/* why */
.why{top:2930px;height:310px;background:var(--charcoal)}
.why .heading{top:62px;color:var(--white)}
.why .heading .soft{color:var(--concrete)}
.why .intro{top:110px;font-size:11px;color:#e2e2e2}
.reason{position:absolute;top:158px;display:flex;align-items:flex-start;gap:14px}
.reason .icon{width:88px;height:88px;border-radius:50%;background:var(--white);border:4px solid var(--lime);display:flex;align-items:center;justify-content:center;flex:none}
.reason h3{color:var(--white);font-size:13.5px;font-weight:600;text-transform:uppercase;margin-top:14px;white-space:nowrap}
.reason p{color:#d0d0d0;font-size:9.5px;line-height:1.55;width:180px;margin-top:6px}

/* reviews */
.reviews{top:3240px;height:470px;background:var(--lime)}
.reviews .heading{top:60px;color:var(--white)}
.reviews .heading .soft{color:var(--ink)}
.review{position:absolute;top:174px;width:306px;height:230px;background:var(--white);padding:10px}
.review-inner{border:1px solid #cfcfcf;height:100%;text-align:center;padding:62px 16px 0}
.avatar{position:absolute;left:106px;top:-47px;width:94px;height:94px;border-radius:50%;border:4px solid var(--white);background:radial-gradient(circle at 50% 40%,#b4a08c,#5c5248)}
.stars{color:#f2b51d;font-size:14px;letter-spacing:2px;position:absolute;left:0;width:100%;top:58px}
.review h4{font-size:13.5px;font-weight:600;text-transform:uppercase;margin-top:24px}
.review p{font-size:11px;font-style:italic;line-height:1.65;color:#444;margin-top:8px}

/* contact */
.connect{top:3710px;height:492px;background:var(--paper)}
.connect .heading{left:122px;top:58px;font-size:34px}
.connect .heading .soft{color:var(--concrete)}
.connect .sub{left:122px;top:103px;font-size:11px;color:#333}
.field{position:absolute;left:122px;width:413px;height:38px;background:var(--concrete-light);color:var(--white);font-size:11px;padding:10px 14px}
.connect .btn{left:122px;top:368px;width:161px;height:39px}
.contact-ring{left:697px;top:56px;width:376px;height:376px;border-radius:50%;border:8px solid var(--lime)}
.contact-photo{left:711px;top:70px;width:348px;height:348px;border-radius:50%;background:radial-gradient(circle at 55% 45%,#f4f4f4 0%,#c9d3dc 45%,#6f8aa3 100%)}
.connect .wordmark{left:6px;top:446px}

/* footer */
.site-footer{top:4202px;height:282px;background:var(--footer);color:var(--white)}
.site-footer .brand{left:122px;top:55px;font-size:15px}
.footer-about{left:122px;top:93px;width:240px;font-size:9.5px;line-height:1.65;color:#d8d8d8}
.footer-col{position:absolute;top:52px}
.footer-col h5{font-family:"Syncopate",sans-serif;font-weight:700;font-size:14px;text-transform:uppercase;letter-spacing:1px;white-space:nowrap}
.footer-col h5 .soft{color:var(--concrete)}
.footer-col ul{list-style:none;margin-top:20px}
.footer-col li{font-size:9.5px;color:#d8d8d8;line-height:19.5px}
.contact-list li{display:flex;align-items:center;gap:10px;line-height:1.3;margin-bottom:12px}
.dot{width:18px;height:18px;border-radius:50%;border:1px solid #d8d8d8;display:flex;align-items:center;justify-content:center;flex:none}
.rule{left:122px;top:217px;width:956px;height:1px;background:#4a4a4a}
.copyright{left:0;width:1200px;top:240px;text-align:center;font-size:9.5px;color:#cfcfcf}
</style>
</head>
<body>

<header class="hero">
  <div class="abs hero-bg" role="img" aria-label="Earthworks site with excavated ground, fencing and surrounding buildings"></div>
  <div class="abs hero-shade"></div>
  <div class="brand">HARBOURGATE EARTHMOVING</div>
  <nav class="nav">
    <a class="active" style="left:510px">Home</a>
    <a style="left:580px">About Us</a>
    <a style="left:671px">Services</a>
    <a style="left:758px">Project</a>
    <a style="left:840px">Contact Us</a>
  </nav>
  <div class="btn" style="left:942px;top:30px;width:136px;height:28px;font-size:10px">Connect With Us</div>
  <div class="abs welcome">Welcome to</div>
  <h1 class="abs title">HARBOURGATE<br>EARTH<br>MOVING</h1>
  <p class="abs tag">a Sydney-based earthworks and excavation company.</p>
  <div class="btn">Discover Our Services</div>
</header>

<section class="about">
  <div class="abs about-ring"></div>
  <div class="abs about-photo" role="img" aria-label="Excavator working on site with crew in high-visibility vests"></div>
  <div class="abs badge">
    <svg width="34" height="34" viewBox="0 0 34 34"><circle cx="17" cy="14" r="10" fill="none" stroke="#fff" stroke-width="3"/><path d="M10 22l-3 10 6-3 4 4 0-8M24 22l3 10-6-3-4 4" fill="none" stroke="#fff" stroke-width="2"/></svg>
    40 years<br>Experience
  </div>
  <h2 class="heading">About <span class="soft">Us</span></h2>
  <div class="abs copy">
    <p>We are a trusted leader in earthworks and excavation services, delivering precision, safety, and reliability to projects of all sizes. With a team of skilled operators and a fleet of modern equipment, we specialize in site preparation, land clearing, trenching, grading, and bulk excavation for residential, commercial, and civil construction.</p>
    <p>Harbourgate Earthmoving is your go-to partner for dependable, high-quality excavation solutions.</p>
  </div>
  <div class="btn">Read More</div>
  <div class="wordmark">HARBOURGATEEARTH</div>
</section>

<section class="services">
  <h2 class="heading centered">Services <span class="soft">We Offer</span></h2>
  <div class="arrow" style="left:86px;top:242px"><svg width="10" height="10" viewBox="0 0 10 10"><path d="M7 1L3 5l4 4" fill="none" stroke="#555" stroke-width="1.6"/></svg></div>
  <div class="arrow" style="left:1088px;top:242px"><svg width="10" height="10" viewBox="0 0 10 10"><path d="M3 1l4 4-4 4" fill="none" stroke="#555" stroke-width="1.6"/></svg></div>

  <div class="service-card" style="left:122px">
    <div class="photo" role="img" aria-label="Orange excavator on a rocky bulk dig" style="background:linear-gradient(170deg,#6f9bc4 0%,#9a6e45 55%,#3b352f 100%)"></div>
    <div class="fade"></div>
    <div class="service-icon"><svg width="26" height="26" viewBox="0 0 26 26"><rect x="3" y="15" width="14" height="6" rx="2" fill="var(--lime)"/><path d="M10 15l5-9 7 4-3 5" fill="none" stroke="var(--lime)" stroke-width="2.4"/></svg></div>
    <div class="service-name">Bulk Excavation</div>
    <div class="btn">Read More</div>
  </div>
  <div class="service-card" style="left:366px">
    <div class="photo" role="img" aria-label="Excavators digging a detailed trench" style="background:linear-gradient(170deg,#b9c7d3 0%,#8a6a4c 55%,#3a2e25 100%)"></div>
    <div class="fade"></div>
    <div class="service-icon"><svg width="26" height="26" viewBox="0 0 26 26"><rect x="4" y="14" width="18" height="7" rx="2" fill="var(--lime)"/><rect x="9" y="6" width="8" height="8" fill="var(--lime)"/></svg></div>
    <div class="service-name">Detailed Excavation</div>
    <div class="btn">Read More</div>
  </div>
  <div class="service-card active" style="left:608px">
    <div class="photo" role="img" aria-label="Excavator demolishing a concrete building" style="background:linear-gradient(170deg,#a8adb1 0%,#6f7275 50%,#2e3032 100%)"></div>
    <div class="fade" style="background:rgba(0,0,0,.45)"></div>
    <div class="service-name">Demolition</div>
    <div class="service-desc">We are a trusted demolition contractor delivering safe, efficient, and compliant demolition solutions for residential, commercial, and industrial projects.</div>
    <div class="btn">Read More</div>
  </div>
  <div class="service-card" style="left:850px">
    <div class="photo" role="img" aria-label="Concrete shoring piles on a basement site" style="background:linear-gradient(170deg,#cfd3d6 0%,#9b9286 50%,#4a443c 100%)"></div>
    <div class="fade"></div>
    <div class="service-icon"><svg width="26" height="26" viewBox="0 0 26 26"><path d="M13 3l9 5-9 5-9-5z" fill="var(--lime)"/><path d="M4 13l9 5 9-5M4 18l9 5 9-5" fill="none" stroke="var(--lime)" stroke-width="2"/></svg></div>
    <div class="service-name">Shoring</div>
    <div class="btn">Read More</div>
  </div>
</section>

<section class="team">
  <div class="abs team-photo-band" role="img" aria-label="Company utility vehicles and trucks parked in a row"></div>
  <h2 class="heading centered">Meet Our <span class="soft">Team</span></h2>
  <p class="abs intro">Our commitment to excellence is grounded in years of industry experience and a deep understanding of terrain, soil conditions, and project demands. We pride ourselves on completing projects on time and within budget, while maintaining the highest standards of environmental stewardship and workplace safety.</p>
  <div class="member" style="left:124px"><div class="ring"><div class="face" role="img" aria-label="Portrait of team member Maya Ferris" style="background:linear-gradient(160deg,#e0e6ea,#8f7a66)"></div></div><div class="name">Maya Ferris</div><div class="bio">View Bio</div></div>
  <div class="member" style="left:319px"><div class="ring"><div class="face" role="img" aria-label="Portrait of team member Owen Darcy" style="background:linear-gradient(160deg,#6f8a5f,#b9b24a)"></div></div><div class="name">Owen Darcy</div><div class="bio">View Bio</div></div>
  <div class="member" style="left:514px"><div class="ring"><div class="face" role="img" aria-label="Portrait of team member Rafi Kahler" style="background:linear-gradient(160deg,#8f8a84,#d8732e)"></div></div><div class="name">Rafi Kahler</div><div class="bio">View Bio</div></div>
  <div class="member" style="left:709px"><div class="ring"><div class="face" role="img" aria-label="Portrait of team member Lucas Brenner" style="background:linear-gradient(160deg,#e6b43a,#6b8db0)"></div></div><div class="name">Lucas Brenner</div><div class="bio">View Bio</div></div>
  <div class="member" style="left:903px"><div class="ring"><div class="face" role="img" aria-label="Portrait of team member Declan Rourke" style="background:linear-gradient(160deg,#e0782e,#7b8e98)"></div></div><div class="name">Declan Rourke</div><div class="bio">View Bio</div></div>
</section>

<section class="projects">
  <h2 class="heading centered">Explore Our <span class="soft">Projects</span></h2>
  <p class="abs intro">Whether it’s preparing a site for a new home, managing large-scale infrastructure works, or supporting road and utility installations, our project portfolio stretches across Sydney, serving clients with tailored earthworks and excavation solutions.</p>
  <div class="project" style="left:122px;top:176px"><div class="photo" role="img" aria-label="Residential excavation pit among trees" style="inset:0;background:linear-gradient(170deg,#7d9ab8 0%,#5c6b3f 35%,#9b7a55 70%,#5b4a3a 100%)"></div><div class="label">Project 1</div></div>
  <div class="project" style="left:610px;top:176px"><div class="photo" role="img" aria-label="Levelled site with boundary fencing" style="inset:0;background:linear-gradient(170deg,#c4ccd3 0%,#c9b9a1 30%,#6b5b4b 70%,#3e342c 100%)"></div><div class="label">Project 2</div></div>
  <div class="project" style="left:122px;top:456px"><div class="photo" role="img" aria-label="Excavator loading a truck on a demolition site" style="inset:0;background:linear-gradient(170deg,#b4bcc3 0%,#d4b23a 40%,#7a6f66 70%,#4a4440 100%)"></div><div class="label">Project 3</div></div>
  <div class="project" style="left:610px;top:456px"><div class="photo" role="img" aria-label="Excavator on open earthworks with city skyline" style="inset:0;background:linear-gradient(180deg,#7fb0e0 0%,#a9cbe8 40%,#b89b78 62%,#7a6249 100%)"></div><div class="label">Project 4</div></div>
  <div class="btn">View All Project</div>
  <div class="wordmark">HARBOURGATEEARTH</div>
</section>

<section class="why">
  <div class="abs" role="img" aria-label="Faded excavator silhouette on a dark background" style="inset:0;background:radial-gradient(ellipse at 60% 20%,#4a4b4c 0%,rgba(51,52,53,0) 60%)"></div>
  <h2 class="heading centered">Why <span class="soft">Choose</span> Us</h2>
  <p class="abs centered intro">We bring more than just machinery to the job — we bring expertise, reliability, and a commitment to excellence.</p>
  <div class="reason" style="left:124px">
    <div class="icon"><svg width="42" height="42" viewBox="0 0 24 24"><path d="M12 21s-8-5.2-8-11a4.5 4.5 0 0 1 8-2.8A4.5 4.5 0 0 1 20 10c0 5.8-8 11-8 11z" fill="var(--lime)"/></svg></div>
    <div><h3>A Heart For People</h3><p>Nullam sit amet ligula eu neque ul trices placerat. Praesent facilisis elit cursus purus mattis scelerisque.</p></div>
  </div>
  <div class="reason" style="left:449px">
    <div class="icon"><svg width="42" height="42" viewBox="0 0 24 24"><ellipse cx="12" cy="12" rx="8" ry="9" fill="var(--lime)"/><path d="M12 3v18M8 8c1 1 1 3 0 4M16 8c-1 1-1 3 0 4M8 14c1 1 1 2 0 3M16 14c-1 1-1 2 0 3" fill="none" stroke="#fff" stroke-width="1.2"/></svg></div>
    <div><h3>A Mind For Innovation</h3><p>Nullam sit amet ligula eu neque ul trices placerat. Praesent facilisis elit cursus purus mattis scelerisque.</p></div>
  </div>
  <div class="reason" style="left:801px">
    <div class="icon"><svg width="44" height="44" viewBox="0 0 24 24"><path d="M2 12s4-7 10-7 10 7 10 7-4 7-10 7S2 12 2 12z" fill="var(--lime)"/><circle cx="12" cy="12" r="4" fill="#fff"/><circle cx="12" cy="12" r="2.2" fill="var(--lime)"/></svg></div>
    <div><h3>An Eye For Safety</h3><p>Nullam sit amet ligula eu neque ul trices placerat. Praesent facilisis elit cursus purus mattis scelerisque.</p></div>
  </div>
</section>

<section class="reviews">
  <h2 class="heading centered">Customer <span class="soft">Reviews</span></h2>
  <div class="arrow" style="left:86px;top:278px"><svg width="10" height="10" viewBox="0 0 10 10"><path d="M7 1L3 5l4 4" fill="none" stroke="#555" stroke-width="1.6"/></svg></div>
  <div class="arrow" style="left:1088px;top:278px"><svg width="10" height="10" viewBox="0 0 10 10"><path d="M3 1l4 4-4 4" fill="none" stroke="#555" stroke-width="1.6"/></svg></div>
  <article class="review" style="left:122px">
    <div class="avatar" role="img" aria-label="Reviewer portrait"></div>
    <div class="review-inner"><div class="stars">★★★★★</div><h4>Tomas Ellery</h4><p>“Suspendisse suscipit id sapien eget blandit. Class aptent taciti sociosqu ad litora torquent per conubia nostra, per inceptos himenaeos. Donec ornare nulla nec tellus pulvinar comm odo. Sed iaculis orci eu purus accumsan.”</p></div>
  </article>
  <article class="review" style="left:449px">
    <div class="avatar" role="img" aria-label="Reviewer portrait"></div>
    <div class="review-inner"><div class="stars">★★★★★</div><h4>Graham Pettit</h4><p>“Sit amet sagittis dui fringilla. Integer porttitor odio vel elit efficitur sollicitudin et eget dui. Fusce dictum mi id mi maximus ultrices. Nam libero turpis, suscipit eu libero sed, cursus commodo lacus. Sed blandit.”</p></div>
  </article>
  <article class="review" style="left:775px">
    <div class="avatar" role="img" aria-label="Reviewer portrait"></div>
    <div class="review-inner"><div class="stars">★★★★★</div><h4>Nathan Colville</h4><p>“Risus sodales dapibus tristique, metus ante commodo leo, et sollicitudin diam nisi sed lorem. Curabitur consectetur eros diam, a dignissim nisi pellentesque id. Curabitur at ipsum ac felis pulvinar tincidunt.”</p></div>
  </article>
</section>

<section class="connect">
  <h2 class="heading"><span class="soft">Connect</span> With Us</h2>
  <p class="abs sub">We’d love to work with you! Be apart of what we’re building.</p>
  <div class="field" style="top:136px">Name</div>
  <div class="field" style="top:190px">Email</div>
  <div class="field" style="top:243px">Phone Number</div>
  <div class="field" style="top:296px;height:57px">Message</div>
  <div class="btn">Send Request</div>
  <div class="abs contact-ring"></div>
  <div class="abs contact-photo" role="img" aria-label="Two engineers in hard hats reviewing plans on a clipboard"></div>
  <div class="wordmark">HARBOURGATEEARTH</div>
</section>

<footer class="site-footer">
  <div class="brand">HARBOURGATE EARTHMOVING</div>
  <p class="abs footer-about">We are a trusted leader in earthworks and excavation services, delivering precision, safety, and reliability to projects of all sizes. With a team of skilled operators and a fleet of Sydney-based earthworks and excavation.</p>
  <div class="footer-col" style="left:427px">
    <h5>Quick <span class="soft">Links</span></h5>
    <ul><li>Home</li><li>About Us</li><li>Services</li><li>Project</li><li>Testimonial</li><li>Contact Us</li></ul>
  </div>
  <div class="footer-col" style="left:672px">
    <h5>Contact <span class="soft">Us</span></h5>
    <ul class="contact-list">
      <li><span class="dot"><svg width="9" height="9" viewBox="0 0 24 24"><path d="M6 2l4 4-2 3c1 3 4 6 7 7l3-2 4 4-3 4C10 22 2 14 2 5z" fill="#fff"/></svg></span>(02) 5550-1842 / (02) 5550-2967</li>
      <li><span class="dot"><svg width="9" height="9" viewBox="0 0 24 24"><rect x="2" y="5" width="20" height="14" fill="none" stroke="#fff" stroke-width="2.5"/><path d="M2 5l10 8 10-8" fill="none" stroke="#fff" stroke-width="2.5"/></svg></span>hello@harbourgate-earth.example</li>
      <li><span class="dot"><svg width="9" height="9" viewBox="0 0 24 24"><path d="M12 2a7 7 0 0 0-7 7c0 5 7 13 7 13s7-8 7-13a7 7 0 0 0-7-7z" fill="#fff"/><circle cx="12" cy="9" r="2.5" fill="#1c1c1c"/></svg></span>42 Quarry Lane, Unit 7<br>Marrickville, NSW 2204</li>
    </ul>
  </div>
  <div class="footer-col" style="left:946px">
    <h5>Follow <span class="soft">Us</span></h5>
    <ul class="contact-list">
      <li><span class="dot"></span>Newsfeed</li>
      <li><span class="dot"></span>Community</li>
      <li><span class="dot"></span>Careers</li>
    </ul>
  </div>
  <div class="abs rule"></div>
  <p class="abs copyright">Copyright © 2025 Harbourgate Earthmoving. All Rights Reserved</p>
</footer>

</body>
</html>
```